Land Buying Company Needs Letterhead for Direct Mail Marketing to Land Owners

We are looking for a professional letterhead that we will be including in our direct mail marketing. We will be sending this to land owners who may be interested in selling or purchasing land.

The letterhead needs to be editable. Headers and footers would look nice, but we are open. We would want it to include our address, website, phone, and email info. For right now the address to use for design purposes would the following:

Address: 415 Bramwell Avenue #600
Dallas, TX 75219
Website - www.quillridgeacres.example
Email - info@quillridgeacres.example
Phone - 866-402-ACRE

I have attached our logo zip file that we just had done on Pixel Guild. Let me know what questions you have, and thank you.

```html
<!DOCTYPE html>
<html lang="en">
<head>
<meta charset="UTF-8">
<title>Quillridge Acres Letterhead</title>
<link rel="stylesheet" href="https://fonts.googleapis.com/css2?family=Montserrat:wght@700&family=Lato:wght@400;700&display=swap">
<style>
  :root {
    --backdrop: #cbcbcb;
    --paper: #ffffff;
    --forest: #44612a;
    --lime: #8dc63f;
    --mist: #e2e1dc;
    --white: #ffffff;
  }
  * { margin: 0; padding: 0; box-sizing: border-box; }
  html, body {
    width: 1200px; height: 1200px; overflow: hidden;
    background: var(--backdrop);
  }
  .letterhead {
    position: absolute; left: 175px; top: 50px;
    width: 850px; height: 1100px;
    background: var(--paper);
    box-shadow: 0 6px 24px rgba(0,0,0,0.18);
    overflow: hidden;
  }
  .brand {
    position: absolute; left: 64px; top: 70px;
    display: flex; align-items: center; gap: 14px;
  }
  .brand-dot {
    width: 58px; height: 58px; border-radius: 50%;
    background: var(--forest);
  }
  .brand-name {
    font-family: "Montserrat", sans-serif; font-weight: 700;
    font-size: 34px; line-height: 1; color: var(--lime);
    letter-spacing: 0.5px;
  }
  .contact {
    position: absolute; right: 64px; top: 78px;
    list-style: none; text-align: right;
    font-family: "Lato", sans-serif; font-weight: 700;
    font-size: 14px; color: var(--lime); letter-spacing: 0.6px;
  }
  .contact li {
    display: flex; justify-content: flex-end; align-items: center;
    gap: 10px; height: 24px;
  }
  .contact-dot {
    width: 14px; height: 14px; border-radius: 50%;
    background: var(--forest);
  }
  .watermark {
    position: absolute; left: 265px; top: 330px;
    width: 360px; height: 360px; border-radius: 50%;
    background: var(--mist);
  }
  .footer {
    position: absolute; left: 0; bottom: 0;
    width: 850px; height: 100px; display: block;
  }
  .footer-address {
    font-family: "Lato", sans-serif; font-weight: 700;
    font-size: 17px; fill: var(--white); letter-spacing: 0.8px;
  }
</style>
</head>
<body>
  <main class="letterhead">
    <header class="brand">
      <span class="brand-dot"></span>
      <span class="brand-name">Quillridge Acres</span>
    </header>

    <ul class="contact">
      <li>866-402-ACRE <span class="contact-dot"></span></li>
      <li>info@quillridgeacres.example <span class="contact-dot"></span></li>
      <li>www.quillridgeacres.example <span class="contact-dot"></span></li>
    </ul>

    <div class="watermark" role="img" aria-label="Faint brand watermark circle"></div>

    <svg class="footer" viewBox="0 0 850 100" aria-label="Footer band with address">
      <polygon class="footer-stripe" points="0,62 420,62 416,72 0,72" fill="var(--lime)"/>
      <polygon class="footer-band" points="0,84 420,84 440,30 850,30 850,100 0,100" fill="var(--forest)"/>
      <text class="footer-address" x="826" y="70" text-anchor="end">415 Bramwell Avenue #600 Dallas, TX 75219</text>
    </svg>
  </main>
</body>
</html>
```